PLOVEN Business Card

Coastal Build Additions and Refits. I need a business card designed for this new high end renovation business. I would like the logo centered on the back side with the ABN (37 915 402 176) on the bottom right hand corner.

I would like the following information placed on the other side along with some customized pattern or design.

Derek Collwood
Director
Phone: 1300 480 957
Fax: (02) 8145 9021
Website: www.plovenbuilders.com.au
Email: d.collwood@plovenbuilders.com.au
PO Box 87,
Kelvinbrook NSW 2069

(FB Logo) PLOVEN - Coastal Build Additions and Refits

The final design should communicate professionalism and trust.

Back side background colour: white
Front side: Undecided

```html
<!DOCTYPE html>
<html lang="en">
<head>
<meta charset="UTF-8">
<title>PLOVEN Business Card</title>
<link rel="stylesheet" href="https://fonts.googleapis.com/css2?family=Open+Sans:wght@400;600;700&display=swap">
<style>
  :root {
    --page-bg: #e6e7ea;
    --card-white: #ffffff;
    --brand-navy: #12325c;
    --brand-blue: #1f5fa3;
    --band-deep: #0b4f8f;
    --band-light: #1a9ee0;
    --swoosh: #1c1c1e;
    --art-fill: #2b2b2d;
    --ink-grey: #555a60;
    --text-light: #ffffff;
    --role-ink: #0d2440;
    --icon-fill: #5b6b7a;
  }
  html, body {
    margin: 0;
    width: 1200px;
    height: 1000px;
    overflow: hidden;
    background: var(--page-bg);
    font-family: "Open Sans", Arial, sans-serif;
  }
  .canvas {
    position: relative;
    width: 1200px;
    height: 1000px;
  }
  .card {
    position: absolute;
    left: 250px;
    width: 700px;
    height: 400px;
    background: var(--card-white);
    box-shadow: 0 6px 18px rgba(0,0,0,0.18);
    overflow: hidden;
  }
  .card--front { top: 60px; }
  .card--back { top: 540px; }
  .card__art {
    position: absolute;
    inset: 0;
    width: 700px;
    height: 400px;
  }
  .brand {
    position: absolute;
    text-align: center;
    width: 300px;
  }
  .brand__name {
    display: block;
    font-weight: 700;
    font-size: 50px;
    letter-spacing: 3px;
    line-height: 1;
    color: var(--brand-navy);
  }
  .brand__tagline {
    display: flex;
    align-items: center;
    gap: 8px;
    margin-top: 8px;
    font-size: 10.5px;
    letter-spacing: 1.2px;
    text-transform: uppercase;
    color: var(--brand-blue);
    white-space: nowrap;
  }
  .brand__tagline::before,
  .brand__tagline::after {
    content: "";
    flex: 1;
    height: 1px;
    background: var(--brand-blue);
  }
  .card--front .brand { top: 40px; right: 28px; }
  .card--back .brand { top: 158px; left: 200px; }

  .holder {
    position: absolute;
    left: 34px;
    top: 96px;
    color: var(--text-light);
  }
  .holder__name {
    margin: 0;
    font-size: 21px;
    font-weight: 700;
    letter-spacing: 0.5px;
    text-transform: uppercase;
  }
  .holder__role {
    margin: 2px 0 0;
    font-size: 13px;
    font-weight: 600;
    color: var(--role-ink);
  }
  .contacts {
    position: absolute;
    left: 150px;
    top: 188px;
    margin: 0;
    padding: 0;
    list-style: none;
    color: var(--text-light);
    font-size: 15px;
    line-height: 1.55;
  }
  .contacts li {
    display: flex;
    align-items: center;
    gap: 10px;
  }
  .contacts .icon {
    width: 14px;
    height: 14px;
    flex: none;
  }
  .contacts .no-icon { padding-left: 24px; }
  .abn {
    position: absolute;
    right: 34px;
    bottom: 26px;
    margin: 0;
    font-size: 14px;
    color: var(--ink-grey);
    letter-spacing: 0.5px;
  }
</style>
</head>
<body>
<main class="canvas">

  <section class="card card--front" aria-label="Business card front">
    <svg class="card__art" viewBox="0 0 700 400" aria-hidden="true">
      <defs>
        <linearGradient id="bandGradient" x1="0" y1="0" x2="0.6" y2="1">
          <stop offset="0" stop-color="#0b4f8f"/>
          <stop offset="1" stop-color="#1a9ee0"/>
        </linearGradient>
      </defs>
      <path class="swoosh" d="M0,48 C270,44 510,170 650,400 L618,400 C480,190 250,62 0,64 Z" fill="#1c1c1e"/>
      <path class="band" d="M0,64 C250,62 480,190 618,400 L0,400 Z" fill="url(#bandGradient)"/>
    </svg>
    <svg class="card__art" viewBox="0 0 700 400" role="img" aria-label="House illustration area">
      <rect x="636" y="330" width="64" height="70" fill="#2b2b2d"/>
    </svg>

    <div class="brand">
      <span class="brand__name">PLOVEN</span>
      <span class="brand__tagline">Coastal Build Additions &amp; Refits</span>
    </div>

    <div class="holder">
      <p class="holder__name">Derek Collwood</p>
      <p class="holder__role">Director</p>
    </div>

    <ul class="contacts">
      <li>
        <svg class="icon" viewBox="0 0 14 14"><rect width="14" height="14" rx="2" fill="#5b6b7a"/><path d="M4 3.5l1.6-.5 1 2.2-1 .8a5 5 0 0 0 2.4 2.4l.8-1 2.2 1-.5 1.6C7 10 4 7 4 3.5z" fill="#fff"/></svg>
        1300 480 957
      </li>
      <li>
        <svg class="icon" viewBox="0 0 14 14"><rect width="14" height="14" rx="2" fill="#5b6b7a"/><rect x="3.5" y="3" width="7" height="3" fill="#fff"/><rect x="3" y="6.5" width="8" height="4.5" fill="#fff"/></svg>
        (02) 8145 9021
      </li>
      <li>
        <svg class="icon" viewBox="0 0 14 14"><rect width="14" height="14" rx="2" fill="#5b6b7a"/><circle cx="7" cy="7" r="4" fill="none" stroke="#fff"/><path d="M3 7h8M7 3v8" stroke="#fff" stroke-width="0.8"/></svg>
        www.plovenbuilders.com.au
      </li>
      <li>
        <svg class="icon" viewBox="0 0 14 14"><rect width="14" height="14" rx="2" fill="#5b6b7a"/><rect x="3" y="4" width="8" height="6" fill="#fff"/><path d="M3 4l4 3.2L11 4" stroke="#5b6b7a" fill="none"/></svg>
        d.collwood@plovenbuilders.com.au
      </li>
      <li>
        <svg class="icon" viewBox="0 0 14 14"><rect width="14" height="14" rx="2" fill="#5b6b7a"/><path d="M7 2.5a3 3 0 0 1 3 3c0 2.3-3 6-3 6s-3-3.7-3-6a3 3 0 0 1 3-3z" fill="#fff"/><circle cx="7" cy="5.5" r="1.1" fill="#5b6b7a"/></svg>
        PO Box 87
      </li>
      <li class="no-icon">Kelvinbrook NSW 2069</li>
    </ul>
  </section>

  <section class="card card--back" aria-label="Business card back">
    <div class="brand">
      <span class="brand__name">PLOVEN</span>
      <span class="brand__tagline">Coastal Build Additions &amp; Refits</span>
    </div>
    <p class="abn">ABN 37 915 402 176</p>
  </section>

</main>
</body>
</html>
```